Tullers Letterhead

I would like to create a letterhead file similar to what we have but in MS Word format. Right now this is a PDF and is not functional

```html
<!DOCTYPE html>
<html lang="en">
<head>
<meta charset="utf-8">
<title>Tullers Hockey Club Letterhead</title>
<link rel="stylesheet" href="https://fonts.googleapis.com/css2?family=Archivo+Black&family=Montserrat:wght@400;500&display=swap">
<style>
  :root {
    --navy: #0d0f3d;
    --gold: #fbb51d;
    --paper: #ffffff;
    --backdrop: #e9e9e9;
    --ink: #22223a;
  }
  html, body {
    margin: 0;
    padding: 0;
    width: 1200px;
    height: 874px;
    overflow: hidden;
    background: var(--backdrop);
  }
  .letterhead {
    position: absolute;
    left: 283px;
    top: 27px;
    width: 634px;
    height: 820px;
    background: var(--paper);
    box-shadow: 0 4px 18px rgba(0,0,0,0.12);
    overflow: hidden;
  }
  .band {
    position: absolute;
    left: 0;
    width: 100%;
    height: 15px;
    background: var(--navy);
  }
  .band--top { top: 0; }
  .band--bottom { bottom: 0; }
  .accent {
    position: absolute;
    background: var(--gold);
  }
  .accent--top-left { left: 18px; top: 0; width: 52px; height: 68px; }
  .accent--bottom-right { right: 14px; bottom: 0; width: 48px; height: 50px; }

  .masthead {
    position: absolute;
    left: 82px;
    top: 28px;
    display: flex;
    align-items: flex-start;
    gap: 14px;
  }
  .club-mark {
    display: flex;
    align-items: center;
    gap: 5px;
    margin-top: 14px;
    white-space: nowrap;
  }
  .club-mark__dot {
    width: 11px;
    height: 11px;
    border-radius: 50%;
    background: var(--gold);
    flex: none;
  }
  .club-mark__name {
    font-family: "Archivo Black", sans-serif;
    font-size: 15px;
    line-height: 1;
    color: var(--navy);
    letter-spacing: 0.4px;
  }
  .club-title {
    white-space: nowrap;
  }
  .club-title__name {
    font-family: "Archivo Black", sans-serif;
    font-size: 13px;
    color: var(--navy);
    margin: 0;
    line-height: 1.1;
  }
  .club-title__city {
    font-family: "Montserrat", sans-serif;
    font-size: 9px;
    line-height: 1.1;
    color: var(--ink);
    margin: 3px 0 0 5px;
    letter-spacing: 0.6px;
  }
  .contact {
    position: absolute;
    right: 28px;
    top: 27px;
    margin: 0;
    padding: 0;
    list-style: none;
    font-family: "Montserrat", sans-serif;
    font-size: 8px;
    color: var(--ink);
    text-align: right;
  }
  .contact__item {
    display: flex;
    justify-content: flex-end;
    align-items: center;
    gap: 5px;
    height: 13px;
    white-space: nowrap;
  }
  .contact__icon {
    width: 9px;
    height: 9px;
    display: block;
  }
</style>
</head>
<body>
  <main class="letterhead">
    <div class="band band--top"></div>
    <div class="accent accent--top-left"></div>

    <header class="masthead">
      <div class="club-mark">
        <span class="club-mark__dot"></span>
        <span class="club-mark__name">TULLERS</span>
      </div>
      <div class="club-title">
        <p class="club-title__name">TULLERS HOCKEY CLUB</p>
        <p class="club-title__city">NORTHFIELD</p>
      </div>
    </header>

    <ul class="contact">
      <li class="contact__item">555-014-0299
        <svg class="contact__icon" viewBox="0 0 10 10" aria-hidden="true">
          <circle cx="5" cy="5" r="5" fill="var(--gold)"/>
          <path d="M3.3 2.6l1 1-.5.6c.3.6.8 1.1 1.4 1.4l.6-.5 1 1-.6.8C4.8 6.6 3.2 5 2.9 3.2z" fill="var(--navy)"/>
        </svg>
      </li>
      <li class="contact__item">northfieldtullers.ca
        <svg class="contact__icon" viewBox="0 0 10 10" aria-hidden="true">
          <circle cx="5" cy="5" r="5" fill="var(--gold)"/>
          <circle cx="5" cy="5" r="2.5" fill="none" stroke="var(--navy)" stroke-width="0.8"/>
          <path d="M2.5 5h5M5 2.5c-1 1.4-1 3.6 0 5M5 2.5c1 1.4 1 3.6 0 5" fill="none" stroke="var(--navy)" stroke-width="0.6"/>
        </svg>
      </li>
      <li class="contact__item">12 Meadow Lane, Northfield AB
        <svg class="contact__icon" viewBox="0 0 10 10" aria-hidden="true">
          <circle cx="5" cy="5" r="5" fill="var(--gold)"/>
          <path d="M5 2.2a1.9 1.9 0 0 1 1.9 1.9C6.9 5.5 5 7.8 5 7.8S3.1 5.5 3.1 4.1A1.9 1.9 0 0 1 5 2.2z" fill="var(--navy)"/>
          <circle cx="5" cy="4.1" r="0.7" fill="var(--gold)"/>
        </svg>
      </li>
    </ul>

    <div class="accent accent--bottom-right"></div>
    <div class="band band--bottom"></div>
  </main>
</body>
</html>
```